Old Time Store Theme/Signage

Looking for a background design that can be applied across multiple signs that give the feel of "Antique" or "Old Time/Wild West" signage. Need the graphics to include text and must be able to edit in the Adobe CS. Looking for signage that may have been seen on shops in the 1800's or early part of last century. Do not want it to look modern.

Target Market(s)

Retailers that are going for an look of signage from the past.

Industry/Entity Type

Retail

Colors

Designer to choose colors to be used in the design.

Requirements
Must have
• Must be 100% editable to adjust text and sizing. Must look like signage from business in the early 1900s .

```html
<!DOCTYPE html>
<html lang="en">
<head>
<meta charset="utf-8">
<title>Old Time Store Sign</title>
<link rel="stylesheet" href="https://fonts.googleapis.com/css2?family=Alfa+Slab+One&family=Lobster&display=swap">
<style>
  :root {
    --frame-green: #3d6a2a;
    --frame-green-dark: #24431a;
    --frame-green-light: #8a9a55;
    --panel-red: #a8121a;
    --panel-red-bright: #d21c22;
    --panel-red-dark: #5e080c;
    --paint-white: #efede6;
    --shadow-green: #2c5a20;
    --crack-dark: rgba(40, 4, 6, 0.7);
    --crack-light: rgba(225, 215, 205, 0.55);
    --page-bg: #f4f1ea;
  }
  html, body {
    margin: 0;
    padding: 0;
    width: 1200px;
    height: 716px;
    overflow: hidden;
    background: var(--page-bg);
  }
  .sign {
    position: relative;
    width: 1200px;
    height: 716px;
    box-sizing: border-box;
    border: 32px solid var(--frame-green);
    background: var(--frame-green);
  }
  .sign__frame-wear {
    position: absolute;
    inset: -32px;
    pointer-events: none;
    background:
      linear-gradient(90deg, transparent 22%, rgba(170,170,90,0.55) 24%, rgba(170,170,90,0.35) 34%, transparent 36%) top / 100% 32px no-repeat,
      linear-gradient(90deg, transparent 40%, rgba(170,170,90,0.45) 42%, transparent 46%, transparent 70%, rgba(170,170,90,0.35) 72%, transparent 75%) bottom / 100% 32px no-repeat,
      linear-gradient(180deg, transparent 20%, rgba(170,170,90,0.35) 24%, transparent 30%) left / 32px 100% no-repeat,
      linear-gradient(180deg, transparent 55%, rgba(170,170,90,0.35) 60%, transparent 66%) right / 32px 100% no-repeat;
    box-shadow: inset 0 0 0 3px var(--frame-green-dark);
  }
  .sign__panel {
    position: absolute;
    inset: 0;
    overflow: hidden;
    background:
      repeating-linear-gradient(180deg, rgba(0,0,0,0) 0 9px, rgba(60,0,4,0.22) 10px, rgba(0,0,0,0) 12px, rgba(0,0,0,0) 23px, rgba(255,120,120,0.06) 24px, rgba(0,0,0,0) 26px),
      radial-gradient(ellipse at 35% 15%, var(--panel-red-bright) 0%, var(--panel-red) 50%, var(--panel-red-dark) 100%);
    box-shadow: inset 0 0 0 3px var(--frame-green-dark), inset 0 0 50px rgba(0,0,0,0.5);
  }
  .sign__text {
    position: absolute;
    left: 0;
    right: 0;
    margin: 0;
    text-align: center;
    color: var(--paint-white);
    white-space: nowrap;
    line-height: 1;
  }
  .sign__established {
    top: 112px;
    font-family: "Alfa Slab One", serif;
    font-size: 56px;
    letter-spacing: 4px;
    text-shadow: 0 7px 0 var(--shadow-green);
  }
  .sign__title {
    top: 180px;
    font-family: "Lobster", cursive;
    font-size: 176px;
    font-weight: 400;
    text-shadow: 4px 11px 0 var(--shadow-green);
    transform: translateX(22px);
  }
  .sign__tagline {
    top: 420px;
    font-family: "Alfa Slab One", serif;
    font-size: 120px;
    letter-spacing: 6px;
    text-shadow: 0 12px 0 var(--shadow-green);
  }
  .sign__wear {
    position: absolute;
    inset: 0;
    width: 100%;
    height: 100%;
    pointer-events: none;
  }
  .sign__crack { fill: none; stroke-width: 1.2; }
  .sign__crack--dark { stroke: var(--crack-dark); }
  .sign__crack--light { stroke: var(--crack-light); }
  .sign__chip { fill: var(--crack-light); }
</style>
</head>
<body>
  <div class="sign">
    <div class="sign__panel">
      <p class="sign__text sign__established">- EST. 1810 -</p>
      <h1 class="sign__text sign__title">Main text here</h1>
      <p class="sign__text sign__tagline">TAGLINE</p>
      <svg class="sign__wear" viewBox="0 0 1136 652" aria-hidden="true">
        <g class="sign__crack sign__crack--light">
          <path d="M40 60 L70 110 L62 170 L90 230 L84 300"/>
          <path d="M150 20 L170 80 L160 140"/>
          <path d="M260 380 L250 450 L272 520 L262 600"/>
          <path d="M420 470 L410 540 L430 610 L418 652"/>
          <path d="M560 150 L575 210 L565 280 L590 330"/>
          <path d="M700 480 L690 560 L705 640"/>
          <path d="M820 40 L840 100 L828 160 L850 220"/>
          <path d="M960 120 L1000 150 L1060 140 L1110 170"/>
          <path d="M930 300 L990 320 L1040 310 L1100 340"/>
          <path d="M1000 420 L1030 480 L1020 560 L1050 620"/>
          <path d="M330 90 L360 130 L350 190"/>
          <path d="M110 440 L140 500 L130 580"/>
          <path d="M760 330 L800 360 L790 420 L820 470"/>
          <path d="M1080 40 L1060 100 L1090 160"/>
        </g>
        <g class="sign__crack sign__crack--dark">
          <path d="M20 200 L60 230 L50 300 L80 360 L70 430"/>
          <path d="M200 560 L230 600 L220 652"/>
          <path d="M480 20 L500 70 L490 120"/>
          <path d="M640 560 L660 600 L650 652"/>
          <path d="M880 520 L900 580 L890 640"/>
          <path d="M1110 240 L1080 300 L1100 370 L1070 440"/>
          <path d="M300 250 L320 300 L310 340"/>
          <path d="M620 20 L640 60 L630 110"/>
        </g>
        <g class="sign__chip">
          <path d="M1040 130 L1075 122 L1090 138 L1060 146 Z"/>
          <path d="M980 150 L1010 142 L1018 160 L990 164 Z"/>
          <path d="M1080 300 L1110 296 L1108 312 L1086 314 Z"/>
          <path d="M1055 540 L1090 548 L1080 566 L1060 558 Z"/>
          <path d="M760 250 L785 246 L790 262 L768 264 Z"/>
          <path d="M90 300 L104 296 L108 310 L94 312 Z"/>
          <path d="M470 590 L500 586 L498 600 L476 602 Z"/>
          <path d="M1090 420 L1115 416 L1112 432 Z"/>
        </g>
      </svg>
    </div>
    <div class="sign__frame-wear"></div>
  </div>
</body>
</html>
```